Stonebrook Aerial Business Card

We are a new company based in Central Queensland, Australia that uses specalised drones (Velkor Sprayhawk K40) to undertake mainly agricultural operations, like spraying weeds, spraying crops, spreading seed etc. I have attached a Plinto proof of a card I was thinking along the lines of - purely a start point. The drone used in the business card MUST be a Velkor Sprayhawk K40.
I am very open to other ideas, especially fonts and layout. I don't have website etc set up yet.
The images are stock and easily interchangeable, I just ask that any background images reflect the local central Queensland area. The photo of the drone is not even complete (propellers cut off) and I need a new stock photo – I’m not sure if this is an issue, or I can pay for an image if need be. PLEASE FIND AN SPRAYHAWK K40 image - 4 sprayers, not 6.
The logo/business name is very draft and looking for further ideas, ideally incorporating drones or agriculture design elements into the design of the business name. The business name needs work on the graphic/design – it is a draft that I have included, the drone propellers (being a different colour) are DRAFT only and intended for changes. PLEASE DO NOT USE THE DRONE PORPELLER I HAVE USED AS A DRAFT. TRY TO FIND SOMETHING ELSE.. The arrow is a shape and not aligned in any way, I would also like ideas on different fonts and additional elements, like air streams, aviation elements, aviation or country western (farming like) themes and fonts etc.
Ideally looking at staying within the blue, green and yellow colours, keeping with an natural, outdoorsy, environmental feel.

Target Market(s)

Farmers, Agriculture, Local Governments, Land Managers

Industry/Entity Type

Agriculture, Drones, Aviation

Contact Information for Business Card

Agricultural Drone (Velkor Sprayhawk K40), Farming, Business Name.

Font styles to use
Sans Serif

Colors
0054AA
0677BA
7BADD7
CADEEF
E8F1F8
0094D4
00A9DD
6FCCEA
C7EBF8
E9F6FB
00AB8E
00BBA5
67D7C9
C6EFE9
E9F9F6
59FF00
82FF00
B8FF75
E3FFCB
F4FFEA

Requirements
Must have
• Velkor Sprayhawk K40 Drone
Should not have
• Tractors

```html
<!DOCTYPE html>
<html lang="en">
<head>
<meta charset="utf-8">
<title>Stonebrook Aerial – Business Card</title>
<link href="https://fonts.googleapis.com/css2?family=Open+Sans:wght@400;700&family=Staatliches&display=swap" rel="stylesheet">
<style>
  :root {
    --page-bg: #b3b4b6;
    --card-white: #f5f5f3;
    --navy: #2c4563;
    --leaf-green: #3d7a3c;
    --harvest-gold: #c8a033;
    --ink-grey: #555a5e;
    --sky-top: #2f7fc4;
    --sky-low: #a9d4ef;
    --mesa: #8a4a2a;
    --field-green: #4f8f2c;
    --field-dark: #1f4f22;
    --white: #ffffff;
  }
  * { margin: 0; padding: 0; box-sizing: border-box; }
  html, body { width: 1200px; height: 1000px; overflow: hidden; }
  body { background: var(--page-bg); position: relative; font-family: "Open Sans", sans-serif; }

  .card {
    position: absolute;
    width: 652px;
    height: 410px;
    border-radius: 20px;
    overflow: hidden;
  }

  /* Front */
  .card-front { left: 75px; top: 65px; }
  .front-scene {
    position: absolute; inset: 0;
    background: linear-gradient(180deg,
      var(--sky-top) 0%, var(--sky-low) 30%,
      var(--mesa) 42%, #c9963f 52%,
      var(--field-green) 62%, var(--field-dark) 100%);
  }
  .front-wordmark {
    position: absolute; left: 0; right: 0; top: 168px;
    text-align: center;
    font-family: "Staatliches", sans-serif;
    color: var(--white);
    line-height: 0.95;
  }
  .front-wordmark .name-main { display: block; font-size: 96px; letter-spacing: 2px; }
  .front-wordmark .name-sub { display: block; font-size: 62px; letter-spacing: 3px; margin-top: 4px; }
  .front-tagline {
    position: absolute; left: 0; right: 0; top: 352px;
    text-align: center;
    font-family: "Staatliches", sans-serif;
    font-size: 30px; letter-spacing: 1.5px;
    color: var(--white);
  }

  /* Back */
  .card-back { left: 481px; top: 535px; background: var(--card-white); }
  .brand-lockup {
    position: absolute; left: 36px; top: 60px; width: 300px;
    text-align: center;
  }
  .brand-disc { display: block; margin: 0 auto; }
  .brand-name {
    margin-top: 14px;
    font-family: "Staatliches", sans-serif;
    font-size: 34px; letter-spacing: 2px;
    color: var(--navy);
  }
  .brand-region {
    margin-top: 2px;
    font-family: "Staatliches", sans-serif;
    font-size: 17px; letter-spacing: 3px;
    color: var(--harvest-gold);
  }
  .contact {
    position: absolute; left: 364px; top: 112px; width: 224px;
    text-align: center;
  }
  .contact-name { font-weight: 700; font-size: 25px; color: var(--leaf-green); letter-spacing: 0.5px; white-space: nowrap; }
  .contact-title { font-size: 19px; color: var(--harvest-gold); line-height: 1.2; }
  .contact-icons { display: flex; justify-content: center; gap: 4px; margin: 8px 0 6px; }
  .contact-phone { font-size: 23px; color: var(--ink-grey); line-height: 1.2; }
  .contact-email { font-size: 15px; color: var(--ink-grey); white-space: nowrap; }
  .contact-web { margin-top: 18px; font-size: 22px; color: var(--ink-grey); }
  .contact-web b { font-weight: 700; }
</style>
</head>
<body>

  <section class="card card-front">
    <div class="front-scene" role="img" aria-label="Illustration of Central Queensland farmland: sunny blue sky, red sandstone mesas, grazing cattle and green crop rows with a spray drone"></div>
    <h1 class="front-wordmark">
      <span class="name-main">Stonebrook</span>
      <span class="name-sub">Aerial</span>
    </h1>
    <p class="front-tagline">Spray • Weed • Seed • Feed</p>
  </section>

  <section class="card card-back">
    <div class="brand-lockup">
      <svg class="brand-disc" width="150" height="150" viewBox="0 0 150 150" aria-hidden="true">
        <circle cx="75" cy="75" r="72" fill="#4f8f2c"/>
      </svg>
      <div class="brand-name">Stonebrook Aerial</div>
      <div class="brand-region">Servicing Central Queensland</div>
    </div>

    <div class="contact">
      <div class="contact-name">NAME SURNAME</div>
      <div class="contact-title">Title</div>
      <div class="contact-icons">
        <svg width="32" height="32" viewBox="0 0 32 32" aria-label="Phone">
          <circle cx="16" cy="16" r="15" fill="var(--navy)"/>
          <path d="M11 8.5c1 0 1.6.3 2 1.3l1 2.5c.3.8 0 1.4-.6 1.9l-.8.7c.8 1.8 2.2 3.3 4 4.2l.8-.8c.5-.6 1.2-.8 1.9-.5l2.5 1c1 .4 1.3 1 1.2 2-.3 2-2 3.2-3.8 2.9C13 23 9 19 8.3 12.3c-.2-1.9 1-3.6 2.7-3.8z" fill="#fff"/>
        </svg>
        <svg width="32" height="32" viewBox="0 0 32 32" aria-label="Email">
          <circle cx="16" cy="16" r="15" fill="var(--navy)"/>
          <rect x="8" y="10.5" width="16" height="11" rx="1.5" fill="none" stroke="#fff" stroke-width="1.8"/>
          <path d="M8.5 11.5l7.5 6 7.5-6" fill="none" stroke="#fff" stroke-width="1.8"/>
        </svg>
      </div>
      <div class="contact-phone">123.456 7890</div>
      <div class="contact-email">name@stonebrookaerial.com</div>
      <div class="contact-web"><b>stonebrookaerial</b>.com</div>
    </div>
  </section>

</body>
</html>
```